Events & Entertainment Production Coordination Business Cards

We need a business card for a new company based in Los Angeles called "Bright Harbor Works"
Our company brings people together for events and helps coordinate different productions. We bring artists from a different country to perform or do events in the U.S.
We are looking for something fun, lively, colorful, creative, and simple.
Nothing that looks too crisp, dark, stiff, or modern.
We connect people from different parts of the world, so definitely something eye-catching will be great!
Colors we would like to see are Black, Yellow, Red, White, Brown to name a few. (Feel free to use more!)
(Double-sided is an option also)
Business
Contact Information for Business Card
Contact Information to put on Business Card:
Name
Title
Address - 2 lines
Phone - place for 3 numbers
E-mail
URL

```html
<!DOCTYPE html>
<html lang="en">
<head>
<meta charset="utf-8">
<title>Bright Harbor Works – Business Cards</title>
<link href="https://fonts.googleapis.com/css2?family=Josefin+Sans:wght@400;600&family=Open+Sans:wght@400;600&display=swap" rel="stylesheet">
<style>
  :root {
    --backdrop: #8b8d90;
    --card-black: #0a0908;
    --card-white: #fbfaf7;
    --sun-yellow: #f2b632;
    --logo-brown: #4b3b31;
    --accent-red: #b0252a;
    --text-dark: #3a2f29;
    --text-soft: #5a504a;
    --rule-warm: #d9c9a8;
    --decor-tint: #ecebe8;
  }
  * { margin: 0; padding: 0; box-sizing: border-box; }
  html, body { width: 1200px; height: 864px; overflow: hidden; }
  body {
    background: var(--backdrop);
    font-family: "Open Sans", sans-serif;
    position: relative;
  }
  .card {
    position: absolute;
    left: 300px;
    width: 600px;
    height: 343px;
    border-radius: 3px;
    box-shadow: 0 8px 22px rgba(0,0,0,.28);
    overflow: hidden;
  }
  .card--front { top: 62px; background: var(--card-black); }
  .card--back { top: 460px; background: var(--card-white); }

  .wordmark {
    position: absolute;
    display: flex;
    flex-direction: column;
    align-items: center;
  }
  .wordmark__line {
    display: flex;
    align-items: center;
    gap: 12px;
  }
  .wordmark__dot {
    width: 18px; height: 18px;
    border-radius: 50%;
    flex: none;
  }
  .wordmark__name {
    font-family: "Josefin Sans", sans-serif;
    font-weight: 600;
    letter-spacing: 1px;
    white-space: nowrap;
    line-height: 1;
    padding-top: 6px;
  }
  .wordmark__rule { height: 2px; margin-top: 10px; }

  .card--front .wordmark { left: 0; right: 0; top: 138px; }
  .card--front .wordmark__name { color: var(--sun-yellow); font-size: 38px; }
  .card--front .wordmark__dot { background: var(--accent-red); width: 22px; height: 22px; }
  .card--front .wordmark__rule { width: 430px; background: var(--accent-red); }

  .card--back .wordmark { right: 28px; top: 36px; align-items: flex-end; }
  .card--back .wordmark__name { color: var(--logo-brown); font-size: 30px; }
  .card--back .wordmark__dot { background: var(--accent-red); }
  .card--back .wordmark__rule { width: 330px; background: var(--sun-yellow); }

  .backdrop-decor {
    position: absolute;
    left: -40px; top: -20px;
    width: 300px; height: 300px;
    border-radius: 50%;
    background: radial-gradient(circle, var(--decor-tint) 0%, var(--decor-tint) 55%, rgba(236,235,232,0) 72%);
  }

  .holder { position: absolute; left: 40px; top: 104px; }
  .holder__name { color: var(--accent-red); font-weight: 600; font-size: 20px; line-height: 1.2; }
  .holder__title { color: var(--text-soft); font-size: 12.5px; line-height: 1.3; }

  .divider {
    position: absolute;
    left: 40px; right: 24px; top: 160px;
    height: 1px; background: var(--rule-warm);
  }

  .address {
    position: absolute;
    left: 40px; bottom: 30px;
    display: flex; gap: 8px; align-items: flex-start;
    color: var(--text-dark);
    font-size: 13px;
    line-height: 20px;
  }
  .address svg { margin-top: 2px; }

  .contacts {
    position: absolute;
    right: 26px; top: 192px;
    list-style: none;
  }
  .contacts li {
    display: flex; justify-content: flex-end; align-items: center;
    gap: 8px;
    color: var(--text-dark);
    font-size: 14px;
    line-height: 22px;
  }
  .card svg { width: 16px; height: 16px; display: block; flex: none; }
</style>
</head>
<body>
  <section class="card card--front" aria-label="Card front">
    <div class="wordmark">
      <div class="wordmark__line">
        <span class="wordmark__dot"></span>
        <span class="wordmark__name">BRIGHT HARBOR WORKS</span>
      </div>
      <span class="wordmark__rule"></span>
    </div>
  </section>

  <section class="card card--back" aria-label="Card back">
    <div class="backdrop-decor" role="img" aria-label="Faint brand decoration in light grey"></div>

    <div class="wordmark">
      <div class="wordmark__line">
        <span class="wordmark__dot"></span>
        <span class="wordmark__name">BRIGHT HARBOR WORKS</span>
      </div>
      <span class="wordmark__rule"></span>
    </div>

    <div class="holder">
      <p class="holder__name">Daniel Reyes</p>
      <p class="holder__title">Managing Director</p>
    </div>

    <div class="divider"></div>

    <div class="address">
      <svg viewBox="0 0 16 16" aria-hidden="true"><rect width="16" height="16" rx="3" fill="var(--sun-yellow)"/><path d="M8 3a3.2 3.2 0 0 0-3.2 3.2C4.8 8.6 8 13 8 13s3.2-4.4 3.2-6.8A3.2 3.2 0 0 0 8 3z" fill="var(--logo-brown)"/><circle cx="8" cy="6.2" r="1.2" fill="var(--sun-yellow)"/></svg>
      <p>1450 Sunset Avenue, Suite 210<br>Los Angeles, CA 90026</p>
    </div>

    <ul class="contacts">
      <li>123-456-7890
        <svg viewBox="0 0 16 16" aria-hidden="true"><rect width="16" height="16" rx="3" fill="var(--accent-red)"/><path d="M3.5 6.5c0-2 9-2 9 0v1h-2.5v-1h-4v1H3.5z M5 8h6l1 4H4z" fill="#fff"/></svg>
      </li>
      <li>123-456-7890
        <svg viewBox="0 0 16 16" aria-hidden="true"><rect width="16" height="16" rx="3" fill="var(--accent-red)"/><path d="M3.5 6.5c0-2 9-2 9 0v1h-2.5v-1h-4v1H3.5z M5 8h6l1 4H4z" fill="#fff"/></svg>
      </li>
      <li>123-456-7890
        <svg viewBox="0 0 16 16" aria-hidden="true"><rect width="16" height="16" rx="3" fill="var(--accent-red)"/><path d="M3.5 6.5c0-2 9-2 9 0v1h-2.5v-1h-4v1H3.5z M5 8h6l1 4H4z" fill="#fff"/></svg>
      </li>
      <li>info@youremail.com
        <svg viewBox="0 0 16 16" aria-hidden="true"><rect width="16" height="16" rx="3" fill="var(--accent-red)"/><rect x="3.5" y="5" width="9" height="6.5" fill="#fff"/><path d="M3.5 5l4.5 3.5L12.5 5" fill="none" stroke="var(--accent-red)" stroke-width="1"/></svg>
      </li>
      <li>www.website.com
        <svg viewBox="0 0 16 16" aria-hidden="true"><rect width="16" height="16" rx="3" fill="var(--accent-red)"/><path d="M7 9.5l-1.5 1.5a1.6 1.6 0 0 1-2.3-2.3L5 7M9 6.5l1.5-1.5a1.6 1.6 0 0 1 2.3 2.3L11 9M6.5 9.5l3-3" fill="none" stroke="#fff" stroke-width="1.3" stroke-linecap="round"/></svg>
      </li>
    </ul>
  </section>
</body>
</html>
```